Maltrey Pools & Patio Homepage Design

I am looking for someone to design a one-page website for a company called Maltrey Pools & Patio. While the content will be different, the design should be similar to https://maltrey-example.com/pools-patio/.
Industry/Entity Type
Pool Cleaning Service
Number of Pages Required
1 page
Font styles to use
- See brand guidelines

Requirements
Must have
- Must be similar in style https://maltrey-example.com/pools-patio/. Look at the Word Doc for the content.

```html
<!DOCTYPE html>
<html lang="en">
<head>
<meta charset="utf-8">
<title>Maltrey Pools & Patio</title>
<link href="https://fonts.googleapis.com/css2?family=Comfortaa:wght@400;600&family=Roboto:wght@300;400;500&display=swap" rel="stylesheet">
<style>
:root{
  --blue:#1e88e5;
  --blue-dark:#1a73d1;
  --green:#76c925;
  --green-light:#9ed957;
  --green-pale:#e2f3cf;
  --sky:#eef6fb;
  --card1:#c4e2f5;
  --card2:#9ccfee;
  --card3:#6fb6e6;
  --text:#3a3a3a;
  --footer:#2b2b2b;
  --white:#fff;
}
*{margin:0;padding:0;box-sizing:border-box}
html,body{width:1200px;height:3531px;overflow:hidden}
body{position:relative;font-family:"Roboto",sans-serif;font-weight:300;color:var(--text);background:var(--white)}
.abs{position:absolute}
h2,.display{font-family:"Comfortaa",sans-serif;font-weight:400;color:var(--blue)}
.btn{display:flex;align-items:center;justify-content:center;font-size:15px;font-weight:400;color:var(--white)}
.btn-blue{background:var(--blue)}
.btn-green{background:var(--green)}

.topbar{left:0;top:0;width:1200px;height:48px;background:var(--blue);color:var(--white);font-size:16px;font-weight:400}
.topbar .item{top:14px;display:flex;align-items:center;gap:10px}
.topbar .sep{left:284px;top:10px;width:1px;height:28px;background:rgba(255,255,255,.4)}

.nav{left:0;top:48px;width:1200px;height:85px}
.logo{display:flex;align-items:center;gap:12px;font-family:"Roboto",sans-serif;font-weight:400;font-size:44px;color:var(--blue)}
.logo .mark{width:40px;height:40px;background:var(--green)}
.menu{left:512px;top:33px;display:flex;gap:24px;font-size:16px;font-weight:400;color:#222}

.hero{left:0;top:133px;width:1200px;height:471px;background:linear-gradient(135deg,#0d6fc4,#38a6e8 45%,#1f8fd9)}
.hero-panel{left:549px;top:238px;width:651px;height:233px;background:rgba(118,201,37,.92);clip-path:polygon(38px 0,100% 0,100% 100%,0 100%,0 38px)}
.hero-title{left:549px;top:278px;width:603px;text-align:center;font-size:40px;line-height:50px;color:var(--white)}

.about-text{left:111px;top:768px;width:531px;font-size:15px;line-height:28.5px;text-align:justify}
.about-text p+p{margin-top:9px}

.services{left:0;top:1273px;width:1200px;height:597px;background:var(--sky)}
.card{top:165px;width:318px;height:350px;clip-path:polygon(0 0,100% 40px,100% 100%,0 100%);text-align:center}
.card h3{font-family:"Comfortaa",sans-serif;font-weight:600;font-size:20px;color:#222;margin-top:128px}
.card p{font-size:15px;line-height:28.5px;margin:12px 26px 0;text-align:justify;text-align-last:center}
.card .arrow{position:absolute;left:146px;bottom:20px}
.icon-circle{top:138px;width:106px;height:106px;border-radius:50%;background:var(--white);border:4px solid var(--blue);display:flex;align-items:center;justify-content:center}

.hex{width:199px;height:172px;clip-path:polygon(25% 0,75% 0,100% 50%,75% 100%,25% 100%,0 50%)}
.hex-label{color:var(--white);font-size:21px;font-weight:400;text-align:center;line-height:28px;display:flex;align-items:flex-end;justify-content:center;padding-bottom:20px}

.contact{left:0;top:2789px;width:1200px;height:465px;background:var(--sky)}
.form{left:530px;top:60px;width:560px;height:347px;background:var(--green-light);clip-path:polygon(50px 0,100% 0,100% 100%,0 100%,0 50px)}
.field{height:40px;background:var(--white);font-size:15px;font-weight:400;color:#555;padding:12px 14px}
.check{display:flex;align-items:center;gap:10px;color:var(--white);font-size:16px;font-weight:400}
.check span{width:24px;height:24px;background:var(--white)}

.footer{left:0;top:3254px;width:1200px;height:277px;background:var(--footer);color:#e6e6e6}
.footer h4{font-family:"Comfortaa",sans-serif;font-weight:600;font-size:17px;color:var(--white);margin-bottom:14px}
.footer li{list-style:none;font-size:15px;font-weight:400;line-height:26px}
</style>
</head>
<body>

<header class="abs topbar">
  <div class="abs item" style="left:111px">
    <svg width="22" height="22" viewBox="0 0 24 24" fill="none" stroke="#fff" stroke-width="1.6"><path d="M5 3h4l2 5-2.5 1.5a11 11 0 0 0 6 6L16 13l5 2v4a2 2 0 0 1-2 2A16 16 0 0 1 3 5a2 2 0 0 1 2-2z"/></svg>
    555-014-2290
  </div>
  <div class="abs sep"></div>
  <div class="abs item" style="left:310px">
    <svg width="20" height="22" viewBox="0 0 24 24" fill="none" stroke="#fff" stroke-width="1.6"><path d="M12 22s7-7 7-12a7 7 0 0 0-14 0c0 5 7 12 7 12z"/><circle cx="12" cy="10" r="2.5"/></svg>
    1180 Harbor Lane, Suite 140, Frisco, TX 75034
  </div>
  <svg class="abs" style="left:1064px;top:12px" width="24" height="24" viewBox="0 0 24 24" fill="none" stroke="#fff" stroke-width="2"><circle cx="10" cy="10" r="7"/><path d="M15 15l6 6"/></svg>
</header>

<nav class="abs nav">
  <div class="abs logo" style="left:111px;top:14px"><span class="mark"></span>maltrey</div>
  <div class="abs menu"><span>Home</span><span>Services</span><span>About Us</span><span>Technician</span><span>Contact Us</span></div>
  <div class="abs btn btn-green" style="left:956px;top:21px;width:133px;height:42px">Get a quote</div>
</nav>

<section class="abs hero" role="img" aria-label="Photo of a smiling child in swim cap and goggles swimming underwater in a pool"></section>
<div class="abs hero-panel" style="top:371px"></div>
<h1 class="abs hero-title display" style="top:411px">Keep Your Pool Sparkling<br>With Maltrey!</h1>
<div class="abs btn btn-blue" style="left:785px;top:531px;width:131px;height:42px">Book Now</div>

<h2 class="abs" style="left:111px;top:688px;font-size:42px">About Us</h2>
<div class="abs about-text">
  <p>We're Maltrey Pools &amp; Patio, and we specialize in pool cleaning and repair services that will keep your pool looking its best. Our reliable and professional team is committed to helping you get the most out of your backyard oasis, ensuring it's always ready for all types of fun when you want it. Our weekly pool cleaning service is affordable and ensures that your pool is properly taken care of throughout the swimming season.</p>
  <p>We're Maltrey Pools &amp; Patio, and we specialize in pool cleaning and repair services that will keep your pool looking its best. Our reliable and professional team is committed to helping you get the most out of your backyard oasis, ensuring it's always ready for all types of fun when you want it. Our weekly pool cleaning service is affordable and ensures that your pool is properly taken care of throughout the swimming season.</p>
</div>
<div class="abs btn btn-green" style="left:111px;top:1136px;width:133px;height:41px">Book Now</div>
<svg class="abs" style="left:692px;top:696px" width="400" height="494" viewBox="0 0 400 494" fill="none">
  <path d="M388 14V492H40L2 458V14" stroke="#76c925" stroke-width="2"/>
</svg>
<div class="abs" role="img" aria-label="Photo of children jumping into a pool with inflatable floats" style="left:701px;top:696px;width:388px;height:485px;background:linear-gradient(180deg,#3aa0e6 0%,#6cc0ea 35%,#4f9a5a 60%,#2aa9e0 100%)"></div>
<svg class="abs" style="left:701px;top:696px" width="388" height="485" fill="none"><path d="M8 8H378V480" stroke="#fff" stroke-width="2"/></svg>

<section class="abs services">
  <h2 class="abs" style="left:0;width:1200px;top:50px;text-align:center;font-size:42px">Our Services</h2>
  <div class="abs card" style="left:111px;background:var(--card1)">
    <h3>Pool Cleaning</h3>
    <p>Our weekly service includes chemical balancing, debris removal, wall and step scrubbing, and filter maintenance. Standard chemicals are included in the quoted price.</p>
    <svg class="arrow" width="26" height="16" viewBox="0 0 26 16" fill="none" stroke="#1e88e5" stroke-width="2"><path d="M1 8h23M17 1l7 7-7 7"/></svg>
  </div>
  <div class="abs card" style="left:441px;background:var(--card2)">
    <h3>Pool Maintenance</h3>
    <p>We perform regular checks on all your pool equipment to make sure it runs efficiently and safely.</p>
    <svg class="arrow" width="26" height="16" viewBox="0 0 26 16" fill="none" stroke="#1e88e5" stroke-width="2"><path d="M1 8h23M17 1l7 7-7 7"/></svg>
  </div>
  <div class="abs card" style="left:771px;background:var(--card3)">
    <h3>Pool Repair</h3>
    <p>From plumbing to equipment malfunctions, our qualified technicians can diagnose and repair any pool problem you may have.</p>
    <svg class="arrow" width="26" height="16" viewBox="0 0 26 16" fill="none" stroke="#1e88e5" stroke-width="2"><path d="M1 8h23M17 1l7 7-7 7"/></svg>
  </div>
  <div class="abs icon-circle" style="left:217px">
    <svg width="60" height="50" viewBox="0 0 60 50" fill="none" stroke="#76c925" stroke-width="2.5"><path d="M14 40V14a6 6 0 0 1 12 0M34 40V14a6 6 0 0 1 12 0M14 24h20M14 32h20M4 44c5-4 9 4 14 0s9 4 14 0 9 4 14 0 9 4 12 0"/></svg>
  </div>
  <div class="abs icon-circle" style="left:547px">
    <svg width="54" height="54" viewBox="0 0 54 54" fill="none" stroke="#76c925" stroke-width="2.5"><path d="M8 46L40 14M40 14l4-8 4 4-8 4M46 46L14 14M14 14a6 6 0 1 1-6-6"/></svg>
  </div>
  <div class="abs icon-circle" style="left:877px">
    <svg width="58" height="50" viewBox="0 0 58 50" fill="none" stroke="#76c925" stroke-width="2.5"><rect x="4" y="12" width="34" height="28" rx="3"/><path d="M10 20h22M10 28h22M38 22h14v14H38M44 22v-6M16 12V6h10v6"/></svg>
  </div>
</section>

<svg class="abs" style="left:216px;top:1936px" width="296" height="362" fill="none"><path d="M10 2V338l16 20H292" stroke="#76c925" stroke-width="2"/></svg>
<div class="abs" role="img" aria-label="Portrait photo of the pool technician" style="left:225px;top:1936px;width:283px;height:354px;background:linear-gradient(180deg,#e9e4de 0%,#cdb8a6 45%,#3a4556 100%)"></div>
<div class="abs" style="left:508px;top:1988px;width:492px;height:211px;background:var(--green-pale)"></div>
<div class="abs" style="left:485px;top:2014px;width:474px;height:212px;background:var(--white);box-shadow:0 4px 14px rgba(0,0,0,.08)">
  <h2 style="margin:34px 0 0 27px;font-size:40px">Meet Your Technician</h2>
  <p style="margin:16px 27px 0;font-size:15px;line-height:28.5px">"I understand that keeping your pool clean and well-maintained is a priority for you, which is why I'm committed to providing top-notch pool cleaning and repair services. Let's get started!"</p>
</div>

<h2 class="abs" style="left:0;width:1200px;top:2360px;text-align:center;font-size:42px">Service Area</h2>
<p class="abs" style="left:0;width:1200px;top:2424px;text-align:center;font-size:15px">Currently, we offer services in the Texas cities of</p>

<div class="abs hex" style="left:188px;top:2485px;background:var(--green-pale)"></div>
<div class="abs hex hex-label" role="img" aria-label="Photo of a small town street in Argyle" style="left:194px;top:2503px;background:linear-gradient(180deg,#b8c2cc,#5b5f66)">Argyle</div>
<div class="abs hex" style="left:402px;top:2557px;background:#d2e6f4"></div>
<div class="abs hex hex-label" role="img" aria-label="Photo of a coastal city view in Corinth" style="left:402px;top:2537px;background:linear-gradient(180deg,#8fb3d6,#4b6d8e 60%,#8a7c6c)">Corinth</div>
<div class="abs hex" style="left:605px;top:2485px;background:var(--green-pale)"></div>
<div class="abs hex hex-label" role="img" aria-label="Photo of a town with gardens in Flower Mound" style="left:611px;top:2503px;background:linear-gradient(180deg,#c9d4dc,#7a8a6a 55%,#4d6b3a)">Flower<br>Mound</div>
<div class="abs hex" style="left:819px;top:2557px;background:#d2e6f4"></div>
<div class="abs hex hex-label" role="img" aria-label="Photo of apartment buildings in Lewisville" style="left:819px;top:2537px;background:linear-gradient(180deg,#6ea4da,#a9c7e6 50%,#5e6f80)">Lewisville</div>

<section class="abs contact">
  <h2 class="abs" style="left:110px;top:96px;font-size:42px">Contact Us</h2>
  <p class="abs" style="left:111px;top:168px;width:372px;font-size:15px;line-height:28.5px">Contact us today at Maltrey Pools &amp; Patio, and let's discuss how our professionals can help bridge the gap between what your pool could be and what it actually is! Get ready to have a worry-free experience with quality service delivered right on time so you can start enjoying those waves anytime soon!</p>
  <div class="abs" style="left:111px;top:358px;display:flex;align-items:center;gap:14px;font-size:15px">
    <svg width="22" height="22" viewBox="0 0 24 24" fill="#1e88e5"><path d="M5 2h4l2 5-2.5 1.5a11 11 0 0 0 6 6L16 12l5 2v4a2 2 0 0 1-2 2A17 17 0 0 1 3 4a2 2 0 0 1 2-2z"/></svg>
    <span>Give us a call today at <span style="color:var(--blue);font-weight:400">555-014-2290</span>.</span>
  </div>
  <div class="abs form">
    <div class="abs display" style="left:0;width:560px;top:16px;text-align:center;font-size:30px;color:var(--white);font-weight:600">Lead Form</div>
    <div class="abs field" style="left:27px;top:75px;width:250px">First Name</div>
    <div class="abs field" style="left:284px;top:75px;width:250px">Last Name</div>
    <div class="abs field" style="left:27px;top:126px;width:250px">Email</div>
    <div class="abs field" style="left:284px;top:126px;width:250px">Phone</div>
    <div class="abs" style="left:0;width:560px;top:188px;text-align:center;color:var(--white);font-size:21px;font-weight:400">Preferred Contact Method</div>
    <div class="abs" style="left:155px;top:234px;display:flex;gap:32px">
      <div class="check"><span></span>Call</div>
      <div class="check"><span></span>Text</div>
      <div class="check"><span></span>Email</div>
    </div>
    <div class="abs btn btn-blue" style="left:218px;top:283px;width:133px;height:41px">Book Now</div>
  </div>
</section>

<footer class="abs footer">
  <div class="abs logo" style="left:114px;top:88px;color:var(--white);font-size:48px"><span class="mark" style="background:var(--white)"></span>maltrey</div>
  <div class="abs" style="left:465px;top:65px">
    <h4>Contact</h4>
    <ul>
      <li style="display:flex;gap:14px"><svg width="14" height="20" viewBox="0 0 24 30" fill="#fff" style="margin-top:4px"><path d="M12 0a10 10 0 0 0-10 10c0 8 10 20 10 20s10-12 10-20A10 10 0 0 0 12 0zm0 14a4 4 0 1 1 0-8 4 4 0 0 1 0 8z"/></svg><span>1180 Harbor Lane, Suite 140,<br>Frisco, TX 75034</span></li>
      <li style="display:flex;gap:14px;margin-top:6px"><svg width="16" height="16" viewBox="0 0 24 24" fill="#fff" style="margin-top:5px"><path d="M5 2h4l2 5-2.5 1.5a11 11 0 0 0 6 6L16 12l5 2v4a2 2 0 0 1-2 2A17 17 0 0 1 3 4a2 2 0 0 1 2-2z"/></svg>555-014-2290</li>
    </ul>
  </div>
  <div class="abs" style="left:799px;top:65px">
    <h4>Quick Links</h4>
    <ul><li>Home</li><li>Services</li><li>About Us</li><li>Technician</li></ul>
  </div>
  <div class="abs" style="left:990px;top:65px">
    <h4>Other Links</h4>
    <ul><li>Privacy Policy</li><li>Terms of use</li><li>Cookies</li><li>Contact</li></ul>
  </div>
  <p class="abs" style="left:0;width:1200px;top:244px;text-align:center;font-size:15px;color:#bdbdbd">2023 Maltrey. All Rights Reserved.</p>
</footer>

</body>
</html>
```